Fence Contractor Website Design

We are working with Yardline Works. They are a local fencing and automatic gate installer and in need of a new website design.
Some sites to use for inspiration:
https://pinevalebarrier.example
https://marwickrails.example
https://www.tellurpostsandboards.example
https://www.grovanpaneling.example
Thank you for taking the time to consider designing a website for us. We are web developers based in Stockton, CA, USA. Most of our projects go through the same process. Understanding this process may help you win a project with us. We custom-code all of our websites in-house. We don’t have any requirements as to what tools you use for your design, but we prefer Figma files. For any design that we label as four-stars, we send it to the client for review. The client picks the final design they want us to use. Once we complete this process, we will continue to show additional clients all the four-star sites and purchase them later. Your designs will have multiple chances to sell. For better chances of success, we ask that you follow these guidelines.
IMAGES:
If you use any images or icons in the design, we ask that you have a link to the asset so we can purchase the image/icon. Most of the designs we submit do not have the customer’s images on them unless they have some great images. Be creative; show us the feeling you are trying to portray with your image choices. Use any royalty-free site you choose. We subscribe to Stockvane and mainly use their images, but we can purchase images outside of Stockvane.
PLEASE NOTE: we will not submit designs to clients with watermarks on the images.
FONTS:
We ask that you identify the fonts used in the design. This can be done in a message if you want. We typically use Google Fonts and Stockvane Fonts.
CONTENT:
We're always open to different content and ideas. We often submit designs with stock images so the client can see our vision. We typically take pictures after the website launch to use their images with our vision. Lorem Ipsum is fine for paragraphs, but we ask that you write the headers in correct English. We want to be able to show the vision and identify the sections of the website.
INSPIRATION:
We typically add a couple of links in the brief of websites we like to help you get started in your design.
REVISIONS:
We do not often ask for revisions of the designs unless we see something in the design that may not appeal to the client. If there are slight changes that we want to make, we do that in the development process.
FEEDBACK:
We rarely give feedback on designs during the design process. We are working on many website projects and do not have the time to provide feedback. We usually respond if your request is well thought out and asks specific questions, but a note asking “feedback, please” usually goes unanswered.
Number of Pages Required
1 page
Look and feel
Each slider illustrates characteristics of the customer's brand and the style your logo design should communicate.

```html
<!DOCTYPE html>
<html lang="en">
<head>
<meta charset="utf-8">
<title>Yardline Works — Fencing &amp; Gates</title>
<link href="https://fonts.googleapis.com/css2?family=Montserrat:wght@700;800&family=Roboto:wght@400;500;700&display=swap" rel="stylesheet">
<style>
:root{
  --navy:#1b2756;
  --navy-deep:#141d40;
  --red:#e8141b;
  --red-soft:#fde3e4;
  --ink:#1e2235;
  --text:#3b3f4c;
  --muted:#f3f3f5;
  --white:#fff;
}
*{box-sizing:border-box;margin:0;padding:0}
html,body{width:1200px;height:4043px;overflow:hidden}
body{font-family:'Roboto',sans-serif;color:var(--text);background:var(--white);position:relative}
.abs{position:absolute}
h1,h2,h3{font-family:'Montserrat',sans-serif;color:var(--ink)}
.btn{display:inline-flex;align-items:center;justify-content:center;font:500 14px 'Roboto',sans-serif;text-transform:uppercase;background:var(--red);color:var(--white);text-decoration:none;letter-spacing:.2px}
.btn--soft{background:var(--red-soft);color:var(--red)}
.section-title{font-size:40px;font-weight:800;text-transform:uppercase;text-align:center;line-height:1}
.section-title::after{content:"";display:block;width:86px;height:3px;background:var(--red);margin:10px auto 0}

/* Header */
.topbar__band{left:540px;top:0;width:660px;height:42px;background:var(--navy-deep);clip-path:polygon(35px 0,100% 0,100% 100%,0 100%)}
.topbar__info{left:578px;top:0;height:42px;display:flex;align-items:center;gap:14px;color:#fff;font-size:13px;white-space:nowrap}
.topbar__info span{display:flex;align-items:center;gap:7px}
.topbar__cta{left:944px;top:0;width:176px;height:42px;font-size:15px}
.header{left:0;top:42px;width:1200px;height:83px;background:#fff;border-bottom:1px solid #e4e4e8}
.brand{left:72px;top:0;width:182px;height:194px;background:#fff;z-index:3;clip-path:polygon(0 0,100% 0,100% 78%,50% 100%,0 78%);display:flex;flex-direction:column;align-items:center;justify-content:center;gap:8px;padding-bottom:30px}
.brand__mark{width:26px;height:26px;background:var(--red)}
.brand__name{font:800 20px 'Montserrat',sans-serif;color:var(--navy);text-align:center;line-height:1.1;text-transform:uppercase}
.nav{right:80px;top:42px;height:83px;display:flex;align-items:center;gap:33px;z-index:4}
.nav a{font:500 16px 'Roboto',sans-serif;color:var(--ink);text-decoration:none;text-transform:uppercase}
.nav a.is-active{color:var(--red);border-bottom:2px solid var(--red);padding-bottom:2px}

/* Hero */
.hero{left:0;top:125px;width:1200px;height:645px;background:linear-gradient(180deg,#2f4a23 0%,#5a3c22 38%,#8a5a33 60%,#3f6a2a 100%)}
.hero__shade{left:0;top:125px;width:1200px;height:645px;background:rgba(10,14,30,.38)}
.hero__content{left:0;top:285px;width:1200px;text-align:center;color:#fff}
.hero__eyebrow{font:700 23px 'Montserrat',sans-serif;text-transform:uppercase}
.hero__title{font:800 35px/1.2 'Montserrat',sans-serif;color:#fff;text-transform:uppercase;margin-top:14px}
.hero__lead{font-size:18px;line-height:1.55;margin:20px auto 0;width:720px}
.hero__cta{margin-top:22px;width:132px;height:40px}
.hero__edge{left:0;top:570px;width:1200px;height:202px}

/* Services */
.services__title{left:0;top:848px;width:1200px}
.svc__img{top:883px;height:305px}
.svc__img--a{clip-path:polygon(0 0,100% 68px,100% 100%,0 100%);background:linear-gradient(160deg,#dfe6ec,#f4f5f4 45%,#6f8a4c)}
.svc__img--b{top:929px;height:259px;clip-path:polygon(0 0,50% 32px,100% 0,100% 100%,0 100%);background:linear-gradient(180deg,#7fb0e6,#c8dbe9 45%,#8a8f86 75%,#6c7c55)}
.svc__img--c{clip-path:polygon(0 46px,100% 0,100% 100%,0 100%);background:linear-gradient(160deg,#c86a3c,#b7845e 45%,#9c8a78 75%,#d9d5cf)}
.svc__card{top:1172px;height:221px;background:#fff;box-shadow:0 4px 14px rgba(0,0,0,.12);text-align:center;padding:22px 20px 0}
.svc__card--active{border-bottom:4px solid var(--red)}
.svc__name{font:700 18px 'Roboto',sans-serif;color:var(--ink);text-transform:uppercase}
.svc__text{font-size:15px;line-height:22px;margin-top:10px;color:var(--text)}
.svc__btn{margin-top:14px;width:132px;height:42px}
.arrow{width:24px;height:24px}

/* About */
.about{left:0;top:1500px;width:1200px;height:527px;background:linear-gradient(120deg,#1f2d60,#141d40 55%,#263256)}
.about__brand{left:78px;top:1640px;width:470px;text-align:center;color:#fff}
.about__brand-mark{width:64px;height:64px;background:#fff;margin:0 auto 26px}
.about__brand-name{font:800 56px/1.05 'Montserrat',sans-serif;text-transform:uppercase}
.about__body{left:617px;top:1583px;width:503px;color:#fff}
.about__title{color:#fff;font-size:40px;font-weight:800;text-transform:uppercase}
.about__title::after{content:"";display:block;width:86px;height:3px;background:var(--red);margin-top:14px}
.about__text{font-size:15px;line-height:24px;text-align:justify;margin-top:22px}
.about__btn{margin-top:22px;width:132px;height:42px}

/* Why */
.why{left:0;top:2027px;width:1200px;height:686px;background:var(--muted)}
.why__title{left:80px;top:2130px;font-size:40px;font-weight:800;text-transform:uppercase}
.why__title::after{content:"";display:block;width:86px;height:3px;background:var(--red);margin-top:10px}
.why__item{left:80px;width:540px;display:flex;gap:27px}
.why__hex{width:80px;height:88px;flex:none;background:#fff;clip-path:polygon(50% 0,100% 25%,100% 75%,50% 100%,0 75%,0 25%);display:flex;align-items:center;justify-content:center}
.why__name{font:700 19px 'Roboto',sans-serif;color:var(--ink);text-transform:uppercase;margin-top:8px}
.why__text{font-size:15px;line-height:23px;margin-top:6px}
.why__btn{left:80px;top:2565px;width:176px;height:42px}
.why__img{left:662px;top:2107px;width:458px;height:526px;clip-path:polygon(50% 0,100% 25%,100% 75%,50% 100%,0 75%,0 25%);background:linear-gradient(110deg,#7c8a70,#c5c9c4 40%,#2a2d33 62%,#1a1c20)}

/* Testimonials */
.testi__title{left:0;top:2790px;width:1200px}
.quote{top:2876px;width:323px;height:303px;background:#fff;box-shadow:0 3px 12px rgba(0,0,0,.12);padding:24px 22px 0}
.quote__stars{color:#f6a623;font-size:15px;letter-spacing:2px}
.quote__text{font-size:15px;line-height:22.5px;text-align:justify;margin-top:8px}
.quote__rule{height:1px;background:#e2e2e6;margin-top:16px}
.quote__who{display:flex;align-items:center;gap:14px;margin-top:18px}
.quote__avatar{width:64px;height:64px;border-radius:50%;background:linear-gradient(135deg,#b38b6d,#e3d3c2);flex:none}
.quote__name{font:500 15px 'Roboto',sans-serif;color:var(--ink);text-transform:uppercase}
.quote__place{font-size:13px;color:var(--red);margin-top:4px}

/* CTA */
.cta{left:0;top:3268px;width:1200px;height:400px;background:linear-gradient(180deg,#1b2759,#1d2a55 60%,#2a3140)}
.cta__inner{left:0;top:3360px;width:1200px;text-align:center;color:#fff}
.cta__title{color:#fff;font-size:40px;font-weight:800;text-transform:uppercase}
.cta__title::after{content:"";display:block;width:86px;height:3px;background:var(--red);margin:12px auto 0}
.cta__text{font-size:15px;line-height:24px;width:940px;margin:22px auto 0}
.cta__btn{margin-top:24px;width:216px;height:42px}

/* Footer */
.footer__brand{left:102px;top:3772px;width:190px;height:140px;display:flex;flex-direction:column;align-items:center;justify-content:center;gap:10px}
.footer__brand .brand__mark{width:30px;height:30px}
.footer__brand .brand__name{font-size:24px}
.fcol{top:3728px}
.fcol__title{font:700 18px 'Roboto',sans-serif;color:var(--ink);text-transform:uppercase}
.fcol ul{list-style:none;margin-top:14px}
.fcol li{font-size:15px;line-height:27px;color:var(--text);display:flex;align-items:center;gap:10px}
.fcol li::before{content:"»";color:var(--red);font-size:16px}
.contact{display:flex;align-items:center;gap:16px;margin-top:14px;font-size:15px;line-height:21px}
.contact__icon{width:46px;height:46px;background:var(--red-soft);display:flex;align-items:center;justify-content:center;flex:none}
.footer__rule{left:80px;top:3982px;width:1040px;height:1px;background:#e2e2e6}
.footer__copy{left:0;top:4001px;width:1200px;text-align:center;font-size:12px;color:var(--ink)}
.social{top:3994px;display:flex;gap:10px}
.social span{width:32px;height:32px;border-radius:50%;background:#eceef2;display:block}
.social span:first-child{background:var(--red)}
</style>
</head>
<body>

<!-- Top bar -->
<div class="abs topbar__band"></div>
<div class="abs topbar__info">
  <span><svg width="13" height="13" viewBox="0 0 24 24"><path fill="#e8141b" d="M6.6 10.8a15 15 0 0 0 6.6 6.6l2.2-2.2c.3-.3.7-.4 1-.2 1.1.4 2.3.6 3.6.6.6 0 1 .4 1 1V20c0 .6-.4 1-1 1A17 17 0 0 1 3 4c0-.6.4-1 1-1h3.5c.6 0 1 .4 1 1 0 1.3.2 2.5.6 3.6.1.3 0 .7-.2 1z"/></svg>+1 (555) 014 2290</span>
  <span>|</span>
  <span><svg width="14" height="11" viewBox="0 0 24 18"><path fill="#e8141b" d="M0 0h24v18H0z"/><path fill="none" stroke="#fff" stroke-width="2" d="M1 1l11 8 11-8"/></svg>hello@yardlineworks.example</span>
</div>
<a class="abs btn topbar__cta">Free Estimates</a>

<header class="abs header"></header>
<div class="abs brand">
  <span class="brand__mark"></span>
  <span class="brand__name">Yardline<br>Works</span>
</div>
<nav class="abs nav">
  <a class="is-active">Home</a><a>About Us</a><a>Services</a><a>Projects</a><a>Testimonials</a><a>Blog</a><a>Contact</a>
</nav>

<!-- Hero -->
<div class="abs hero" role="img" aria-label="Photo of a tall wooden privacy fence with black posts along a green lawn"></div>
<div class="abs hero__shade"></div>
<div class="abs hero__content">
  <p class="hero__eyebrow">Welcome to Yardline Works</p>
  <h1 class="hero__title">Strong, Secure, and Stylish Fencing<br>Solutions You Can Trust</h1>
  <p class="hero__lead">At Yardline Works, we specialize in custom fencing and automatic gate installations that enhance security and elevate curb appeal.</p>
  <a class="btn hero__cta">Get Started</a>
</div>
<svg class="abs hero__edge" viewBox="0 0 1200 202" preserveAspectRatio="none">
  <polygon fill="#fff" points="0,34 600,200 1200,34 1200,202 0,202"/>
  <polygon fill="#e8141b" points="0,14 600,180 1200,14 1200,34 600,200 0,34"/>
</svg>

<!-- Services -->
<h2 class="abs section-title services__title">Our Services</h2>
<svg class="abs arrow" style="left:29px;top:1024px" viewBox="0 0 24 24"><path d="M15 4l-8 8 8 8" fill="none" stroke="#9a9aa3" stroke-width="2.5"/></svg>
<svg class="abs arrow" style="left:1144px;top:1024px" viewBox="0 0 24 24"><path d="M9 4l8 8-8 8" fill="none" stroke="#1e2235" stroke-width="2.5"/></svg>

<div class="abs svc__img svc__img--a" style="left:80px;width:328px" role="img" aria-label="Photo of a white vinyl fence in a green garden"></div>
<div class="abs svc__card" style="left:96px;width:296px">
  <h3 class="svc__name">Residential Fencing</h3>
  <p class="svc__text">Lorem ipsum dolor sit amet, consectetur adipiscing elit, sed do eiusmod tempor incididunt ut labore et dolorea.</p>
  <a class="btn btn--soft svc__btn">Learn More</a>
</div>

<div class="abs svc__img svc__img--b" style="left:436px;width:328px" role="img" aria-label="Photo of a commercial construction site with temporary fencing and trucks"></div>
<div class="abs svc__card svc__card--active" style="left:452px;width:296px">
  <h3 class="svc__name">Commercial Fencing</h3>
  <p class="svc__text">Lorem ipsum dolor sit amet, consectetur adipiscing elit, sed do eiusmod tempor incididunt ut labore et dolorea.</p>
  <a class="btn svc__btn">Learn More</a>
</div>

<div class="abs svc__img svc__img--c" style="left:791px;width:328px" role="img" aria-label="Photo of a hand holding a remote in front of an automatic sliding gate"></div>
<div class="abs svc__card" style="left:807px;width:296px">
  <h3 class="svc__name">Automatic Gates</h3>
  <p class="svc__text">Lorem ipsum dolor sit amet, consectetur adipiscing elit, sed do eiusmod tempor incididunt ut labore et dolorea.</p>
  <a class="btn btn--soft svc__btn">Learn More</a>
</div>

<!-- About -->
<section class="abs about" role="img" aria-label="Dark blue-tinted photo of a modern horizontal slat fence beside a driveway"></section>
<div class="abs about__brand">
  <div class="about__brand-mark"></div>
  <div class="about__brand-name">Yardline<br>Works</div>
</div>
<div class="abs about__body">
  <h2 class="about__title">About Us</h2>
  <p class="about__text">Lorem ipsum dolor sit amet, consectetur adipiscing elit, sed do eiusmod tempor incididunt ut labore et dolore magna aliqua. Ut enim ad minim veniam, quis nostrud exercitation ullamco laboris nisi ut aliquip ex ea commodo consequat. Duis aute irure dolor in reprehenderit in voluptate velit esse cillum dolore eu fugiat nulla pariatur.</p>
  <p class="about__text" style="margin-top:14px">Lorem ipsum dolor sit amet, consectetur adipiscing elit, sed do eiusmod tempor incididunt ut labore et dolore magna aliqua. Ut enim ad minim veniam, quis nostrud exercita.</p>
  <a class="btn about__btn">Learn More</a>
</div>

<!-- Why -->
<section class="abs why"></section>
<h2 class="abs why__title">Why Yardline Works?</h2>

<div class="abs why__item" style="top:2210px">
  <div class="why__hex"><svg width="34" height="40" viewBox="0 0 34 40"><circle cx="17" cy="15" r="13" fill="none" stroke="#e8141b" stroke-width="3"/><path d="M17 8l2.2 4.6 5 .6-3.7 3.4 1 5-4.5-2.5-4.5 2.5 1-5-3.7-3.4 5-.6z" fill="#e8141b"/><path d="M9 26l-3 12 6-3 3 4 2-9M25 26l3 12-6-3-3 4-2-9" fill="#e8141b"/></svg></div>
  <div><h3 class="why__name">Experience</h3><p class="why__text">Lorem ipsum dolor sit amet, consectetur adipiscing elit, sed do eiusmod tempor incididunt ipsum dolorea.</p></div>
</div>
<div class="abs why__item" style="top:2321px">
  <div class="why__hex"><svg width="38" height="34" viewBox="0 0 38 34"><g fill="#e8141b"><path d="M3 6l3-5 3 5v28H3zM12 6l3-5 3 5v28h-6zM21 6l3-5 3 5v28h-6zM30 6l3-5 3 5v28h-6z"/><rect x="0" y="10" width="38" height="4"/><rect x="0" y="22" width="38" height="4"/></g></svg></div>
  <div><h3 class="why__name">Premium Materials</h3><p class="why__text">Lorem ipsum dolor sit amet, consectetur adipiscing elit, sed do eiusmod tempor incididuntea.</p></div>
</div>
<div class="abs why__item" style="top:2433px">
  <div class="why__hex"><svg width="40" height="34" viewBox="0 0 40 34"><g fill="#e8141b"><circle cx="20" cy="8" r="6"/><path d="M10 32c0-8 4-13 10-13s10 5 10 13z"/><circle cx="7" cy="12" r="4.5"/><path d="M0 32c0-6 3-10 7-10 2 0 3 .5 4 1.5-1.5 2-2.5 5-2.5 8.5z"/><circle cx="33" cy="12" r="4.5"/><path d="M40 32c0-6-3-10-7-10-2 0-3 .5-4 1.5 1.5 2 2.5 5 2.5 8.5z"/></g></svg></div>
  <div><h3 class="why__name">Customer Satisfaction</h3><p class="why__text">Lorem ipsum dolor sit amet, consectetur adipiscing elit, sed do eiusmod tempor incididunt ipsum dolorea.</p></div>
</div>
<a class="abs btn why__btn">Free Estimates</a>
<div class="abs why__img" role="img" aria-label="Close-up photo of a smart gate keypad mounted on a black metal fence"></div>

<!-- Testimonials -->
<h2 class="abs section-title testi__title">Testimonials</h2>
<svg class="abs arrow" style="left:30px;top:3016px" viewBox="0 0 24 24"><path d="M15 4l-8 8 8 8" fill="none" stroke="#9a9aa3" stroke-width="2.5"/></svg>
<svg class="abs arrow" style="left:1146px;top:3016px" viewBox="0 0 24 24"><path d="M9 4l8 8-8 8" fill="none" stroke="#1e2235" stroke-width="2.5"/></svg>

<article class="abs quote" style="left:82px">
  <div class="quote__stars">★★★★★</div>
  <p class="quote__text">Lorem ipsum dolor sit amet, consectetur adipiscing elit, sed do eiusmod tempor incididunt ut labore et dolore magna aliqu ut enim ad minim veniam, quis nostrud ex citation ullamco laboris nisi ut aliquip ex ea commodo consequat.</p>
  <div class="quote__rule"></div>
  <div class="quote__who"><div class="quote__avatar" role="img" aria-label="Customer portrait"></div><div><div class="quote__name">Dane Holloway</div><div class="quote__place">United States</div></div></div>
</article>
<article class="abs quote" style="left:439px">
  <div class="quote__stars">★★★★★</div>
  <p class="quote__text">Lorem ipsum dolor sit amet, consectetur adipiscing elit, sed do eiusmod tempor incididunt ut labore et dolore magna aliqu ut enim ad minim veniam, quis nostrud ex citation ullamco laboris nisi ut aliquip ex ea commodo consequat.</p>
  <div class="quote__rule"></div>
  <div class="quote__who"><div class="quote__avatar" role="img" aria-label="Customer portrait"></div><div><div class="quote__name">Mara Quinlan</div><div class="quote__place">United States</div></div></div>
</article>
<article class="abs quote" style="left:797px">
  <div class="quote__stars">★★★★★</div>
  <p class="quote__text">Lorem ipsum dolor sit amet, consectetur adipiscing elit, sed do eiusmod tempor incididunt ut labore et dolore magna aliqu ut enim ad minim veniam, quis nostrud ex citation ullamco laboris nisi ut aliquip ex ea commodo consequat.</p>
  <div class="quote__rule"></div>
  <div class="quote__who"><div class="quote__avatar" role="img" aria-label="Customer portrait"></div><div><div class="quote__name">Dane Holloway</div><div class="quote__place">United States</div></div></div>
</article>

<!-- CTA -->
<section class="abs cta" role="img" aria-label="Dusk photo of a house behind a dark wooden fence with a navy overlay"></section>
<div class="abs cta__inner">
  <h2 class="cta__title">Build Your Fence Today!</h2>
  <p class="cta__text">Lorem ipsum dolor sit amet, consectetur adipiscing elit, sed do eiusmod tempor incididunt ut labore et dolore magna aliqua. Ut enim ad minim veniam, quis nostrud exercitation ullamco laboris nisi ut aliquip ex ea commodo consequat. Duis aute irure dolor in reprehenderit in voluptate velit esse cillum dolore eu fugiat nulla pariatur.</p>
  <a class="btn cta__btn">Request a Free Quote</a>
</div>

<!-- Footer -->
<div class="abs footer__brand"><span class="brand__mark"></span><span class="brand__name">Yardline<br>Works</span></div>

<div class="abs fcol" style="left:359px">
  <h3 class="fcol__title">Navigation</h3>
  <ul><li>Home</li><li>About Us</li><li>Services</li><li>Projects</li><li>Testimonials</li><li>Blog</li><li>Contact</li></ul>
</div>
<div class="abs fcol" style="left:543px">
  <h3 class="fcol__title">Quick Links</h3>
  <ul><li>Site Map</li><li>Privacy Policy</li><li>Terms And Conditions</li><li>Disclaimer</li><li>Legal Support</li></ul>
</div>
<div class="abs fcol" style="left:783px;width:340px">
  <h3 class="fcol__title">Contact Us</h3>
  <div class="contact"><span class="contact__icon"><svg width="16" height="20" viewBox="0 0 16 20"><path fill="#e8141b" d="M8 0a8 8 0 0 1 8 8c0 6-8 12-8 12S0 14 0 8a8 8 0 0 1 8-8z"/><circle cx="8" cy="8" r="3" fill="#fde3e4"/></svg></span><span>465, Lorum Ipsum Dolore Sed Ameat,<br>United States</span></div>
  <div class="contact"><span class="contact__icon"><svg width="18" height="18" viewBox="0 0 24 24"><path fill="#e8141b" d="M6.6 10.8a15 15 0 0 0 6.6 6.6l2.2-2.2c.3-.3.7-.4 1-.2 1.1.4 2.3.6 3.6.6.6 0 1 .4 1 1V20c0 .6-.4 1-1 1A17 17 0 0 1 3 4c0-.6.4-1 1-1h3.5c.6 0 1 .4 1 1 0 1.3.2 2.5.6 3.6.1.3 0 .7-.2 1z"/></svg></span><span>+1 (555) 014 2290</span></div>
  <div class="contact"><span class="contact__icon"><svg width="20" height="15" viewBox="0 0 24 18"><path fill="#e8141b" d="M0 0h24v18H0z"/><path fill="none" stroke="#fde3e4" stroke-width="2" d="M1 1l11 8 11-8"/></svg></span><span>hello@yardlineworks.example</span></div>
</div>

<div class="abs footer__rule"></div>
<p class="abs footer__copy">© 2025 YARDLINE WORKS &nbsp;| &nbsp;All Rights Reserved</p>
<div class="abs social" style="left:1003px"><span></span><span></span><span></span></div>

</body>
</html>
```